Business card design for Tolvin Waste

I would like double-sided business cards for myself and my partner that includes our logo and the existing colour scheme. We provide waste and environmental services to customers in the motor-vehicle and engineering industries.

```html
<!DOCTYPE html>
<html lang="en">
<head>
<meta charset="utf-8">
<title>Tolvin Waste – Business Card</title>
<link rel="stylesheet" href="https://fonts.googleapis.com/css2?family=Open+Sans:wght@400;600;700&display=swap">
<style>
  :root {
    --bg: #3a3b3d;
    --paper: #ffffff;
    --green-light: #a6d13a;
    --green: #7cb72e;
    --green-dark: #5e9e2a;
    --ink: #2b2b2b;
    --logo-grey: #3d3f42;
    --rule: #9a9a9a;
  }
  * { margin: 0; padding: 0; box-sizing: border-box; }
  html, body { width: 1200px; height: 896px; overflow: hidden; }
  body {
    background: var(--bg);
    font-family: "Open Sans", Arial, sans-serif;
    color: var(--ink);
    position: relative;
  }
  .card {
    position: absolute;
    left: 250px;
    width: 700px;
    height: 400px;
    overflow: hidden;
    box-shadow: 0 10px 24px rgba(0,0,0,.35);
  }
  .card--front { top: 28px; background: var(--paper); }
  .card--back {
    top: 468px;
    background: radial-gradient(ellipse at 30% 20%, var(--green-light) 0%, var(--green) 55%, var(--green-dark) 100%);
    display: flex; align-items: center; justify-content: center;
  }

  /* front */
  .contact { position: absolute; left: 54px; top: 96px; width: 300px; }
  .contact__name {
    color: var(--green); font-weight: 700; font-size: 26px;
    letter-spacing: .5px; text-transform: uppercase; line-height: 1.1;
  }
  .contact__role { font-size: 18px; margin-top: 2px; }
  .contact__rule { height: 1px; background: var(--rule); margin: 10px 0 10px; width: 300px; }
  .contact__row { display: flex; align-items: center; gap: 8px; font-size: 17px; line-height: 1.45; }
  .contact__row svg { width: 14px; height: 14px; fill: var(--green-dark); flex: none; }

  .brand { position: absolute; left: 380px; top: 110px; display: flex; align-items: center; gap: 14px; }
  .brand__dot { width: 66px; height: 66px; border-radius: 50%; background: var(--green); flex: none; }
  .brand__name {
    font-weight: 700; font-size: 34px; color: var(--logo-grey);
    letter-spacing: 1px; text-transform: uppercase; line-height: 1;
  }

  .address { position: absolute; right: 44px; top: 292px; width: 330px; text-align: right; }
  .address__rule { height: 1px; background: var(--rule); margin-bottom: 10px; }
  .address p { font-size: 17px; line-height: 1.35; }

  .edge-band { position: absolute; left: 0; bottom: 0; width: 700px; height: 22px; }

  /* back */
  .back__name {
    color: var(--paper); font-weight: 700; font-size: 52px;
    letter-spacing: 2px; text-transform: uppercase;
  }
</style>
</head>
<body>

<section class="card card--front" aria-label="Business card front">
  <div class="contact">
    <h1 class="contact__name">Marek Olsen</h1>
    <p class="contact__role">Managing Director</p>
    <div class="contact__rule"></div>
    <p class="contact__row">
      <svg viewBox="0 0 16 16" aria-hidden="true"><path d="M3 1h3l1.5 4-2 1.3a9 9 0 0 0 4.2 4.2L11 8.5l4 1.5v3a2 2 0 0 1-2 2A12 12 0 0 1 1 3a2 2 0 0 1 2-2z"/></svg>
      044-555 210 347
    </p>
    <p class="contact__row">
      <svg viewBox="0 0 16 16" aria-hidden="true"><path d="M4 0h8a1 1 0 0 1 1 1v14a1 1 0 0 1-1 1H4a1 1 0 0 1-1-1V1a1 1 0 0 1 1-1zm1 2v10h6V2zm3 11a1 1 0 1 0 0 2 1 1 0 0 0 0-2z"/></svg>
      044-555 210 347
    </p>
    <p class="contact__row">
      <svg viewBox="0 0 16 16" aria-hidden="true"><path d="M0 3h16v10H0zm1.5 1.3V12h13V4.3L8 9z"/></svg>
      hello@tolvinmail.com
    </p>
  </div>

  <div class="brand">
    <span class="brand__dot"></span>
    <span class="brand__name">Tolvin Waste</span>
  </div>

  <div class="address">
    <div class="address__rule"></div>
    <p>48 Kestrel Road, Unit 7</p>
    <p>Brackton Vale, 204518</p>
  </div>

  <svg class="edge-band" viewBox="0 0 700 22" preserveAspectRatio="none" aria-hidden="true">
    <defs>
      <linearGradient id="bandFill" x1="0" x2="1" y1="0" y2="0">
        <stop offset="0" stop-color="#5e9e2a"/>
        <stop offset="1" stop-color="#a6d13a"/>
      </linearGradient>
    </defs>
    <polygon points="0,4 700,16 700,22 0,22" fill="url(#bandFill)"/>
  </svg>
</section>

<section class="card card--back" aria-label="Business card back">
  <span class="back__name">Tolvin Waste</span>
</section>

</body>
</html>
```